Birchfield Dental Care Stationery

create stationery, business cards and envelops for business. Use current logo on website but open to new fonts for the business name. Business name is Birchfield Dental Care, would like below the name added "Cosmetic - Family - Implants" Website is www.birchfielddentalcareQX.example. I would like to have modern look, clean, and professional. The water mark of the logo is a great thing to ad as well.

Target Market(s)

General public, Families, Cosmetic, Implant

Industry/Entity Type

Dental

Font styles to use
Sans Serif

Colors
9bcb3c
000000
757575
c9c9c9

Requirements
Must have
• Would like to see different versions of the current logo. Improvements, color, sytle, and class.
Nice to have
• current font has double "oo" in the Birchfield logo, does not need to have with new logo.

```html
<!DOCTYPE html>
<html lang="en">
<head>
<meta charset="utf-8">
<title>Birchfield Dental Care Stationery</title>
<link href="https://fonts.googleapis.com/css2?family=Saira+Semi+Condensed:wght@300;400;500&display=swap" rel="stylesheet">
<style>
  :root {
    --green: #9bcb3c;
    --black: #000000;
    --grey: #757575;
    --light: #c9c9c9;
    --faint: #e4e4e4;
    --backdrop: #979797;
    --paper: #ffffff;
    --font: "Saira Semi Condensed", "Arial Narrow", sans-serif;
  }
  * { margin: 0; padding: 0; box-sizing: border-box; }
  html, body { width: 1200px; height: 1200px; overflow: hidden; }
  body { position: relative; background: var(--backdrop); font-family: var(--font); color: var(--black); }

  .sheet { position: absolute; background: var(--paper); overflow: hidden; box-shadow: 3px 4px 8px rgba(0,0,0,.35); }
  .sheet > * { position: absolute; }

  .mark-ring { border-radius: 50%; border: 4px solid var(--green); flex: none; }
  .watermark { border-radius: 50%; border: 14px solid var(--faint); }
  .brand-name { font-weight: 300; color: var(--grey); line-height: .95; white-space: nowrap; }
  .tagline { font-weight: 500; text-transform: uppercase; letter-spacing: .02em; white-space: nowrap; }
  .rule { height: 1px; background: #999; }

  /* Letterhead */
  .letterhead { left: 62px; top: 48px; width: 772px; height: 1090px; }
  .letterhead .mark-ring { left: 56px; top: 56px; width: 80px; height: 80px; }
  .letterhead .brand-name { left: 148px; top: 46px; font-size: 40px; }
  .letterhead .rule { left: 148px; top: 124px; width: 566px; }
  .letterhead .tagline { left: 148px; top: 128px; font-size: 13px; }
  .doctor-tab { right: 58px; top: 96px; height: 28px; padding: 0 8px; background: var(--green); font-size: 17px; font-weight: 500; line-height: 28px; white-space: nowrap; }
  .doctor-title { right: 58px; top: 129px; font-size: 11px; font-weight: 500; white-space: nowrap; }
  .letterhead .watermark { left: 402px; top: 616px; width: 400px; height: 400px; }
  .footer-band { left: 0; top: 1040px; width: 100%; height: 20px; background: var(--light); font-size: 12px; font-weight: 500; letter-spacing: .04em; text-align: center; line-height: 20px; white-space: nowrap; }

  /* Envelope */
  .envelope { left: 196px; top: 290px; width: 841px; height: 364px; }
  .envelope .watermark { left: 608px; top: 114px; width: 248px; height: 248px; border-width: 10px; }
  .envelope .mark-ring { left: 47px; top: 257px; width: 64px; height: 64px; border-width: 3px; }
  .envelope-brand { left: 112px; top: 250px; right: 29px; display: flex; align-items: flex-end; gap: 26px; border-bottom: 1px solid #999; padding-bottom: 2px; }
  .envelope-brand .brand-name { font-size: 32px; }
  .envelope .tagline { left: 112px; top: 315px; font-size: 11px; }
  .return-address { font-size: 10px; font-weight: 500; white-space: nowrap; padding-bottom: 3px; }

  /* Business card */
  .card { left: 806px; top: 173px; width: 340px; height: 202px; }
  .card .watermark { left: 211px; top: 76px; width: 110px; height: 110px; border-width: 6px; }
  .card-header { right: 12px; top: 12px; display: flex; gap: 6px; }
  .card-person { line-height: 1.2; }
  .card-person .name { font-size: 11px; font-weight: 500; white-space: nowrap; }
  .card-person .role { font-size: 7px; color: #333; width: 86px; }
  .card-divider { width: 1px; height: 46px; background: #555; }
  .card-contact { font-size: 7px; line-height: 1.6; white-space: nowrap; }
  .card .mark-ring { left: 26px; top: 123px; width: 52px; height: 52px; border-width: 3px; }
  .card .brand-name { left: 80px; top: 117px; font-size: 21px; }
  .card .rule { left: 78px; top: 166px; width: 262px; }
  .card .tagline { left: 80px; top: 168px; font-size: 7px; }
</style>
</head>
<body>

<section class="sheet letterhead" aria-label="Letterhead">
  <div class="watermark" aria-hidden="true"></div>
  <div class="mark-ring" aria-hidden="true"></div>
  <div class="brand-name">Birchfield<br>Dental Care</div>
  <div class="rule"></div>
  <div class="tagline">Cosmetic - Family - Implants</div>
  <div class="doctor-tab">Dr. Marcus Holloway</div>
  <div class="doctor-title">Larkvale Cosmetic, Family, &amp; Sedation Dentist</div>
  <div class="footer-band">1180 N Birchfield Way Larkvale, QX 55012-3344 | 555-014-2290 | www.birchfielddentalcareQX.example</div>
</section>

<section class="sheet envelope" aria-label="Envelope">
  <div class="watermark" aria-hidden="true"></div>
  <div class="mark-ring" aria-hidden="true"></div>
  <div class="envelope-brand">
    <div class="brand-name">Birchfield<br>Dental Care</div>
    <div class="return-address">1180 N Birchfield Way, Larkvale, QX | 55012-3344 | 555-014-2290 | www.birchfielddentalcareQX.example</div>
  </div>
  <div class="tagline">Cosmetic - Family - Implants</div>
</section>

<section class="sheet card" aria-label="Business card">
  <div class="watermark" aria-hidden="true"></div>
  <div class="card-header">
    <div class="card-person">
      <div class="name">Dr. Marcus Holloway</div>
      <div class="role">Larkvale Cosmetic, Family, &amp; Sedation Dentist</div>
    </div>
    <div class="card-divider"></div>
    <div class="card-contact">1180 N Birchfield Way<br>Larkvale, QX 55012-3344<br>555-014-2290<br>www.birchfielddentalcareQX.example</div>
  </div>
  <div class="mark-ring" aria-hidden="true"></div>
  <div class="brand-name">Birchfield<br>Dental Care</div>
  <div class="rule"></div>
  <div class="tagline">Cosmetic - Family - Implants</div>
</section>

</body>
</html>
```